Emerging Ed-Tech Startup seeking Stationery Designs!

We are in need of basic set of stationery designs to be used for our business operations, letters, emails, and in-office materials. We are a technology startup enhancing on campus work experience offerings by establishing a collaborative work environment for the completion of such tasks.

Our colors are Vibrant Tiffany Blue/Black/White.

Website: www.campusmeridian.com (Still under construction aside from the landing pages)

Please make sure the designs use a brighter more vibrant tiffany blue color than seen in the image files uploaded. We are not using those materials.

Our logo has been added as a file as well, please use that for any designs (include that logo). Thank you.

```html
<!DOCTYPE html>
<html lang="en">
<head>
<meta charset="utf-8">
<title>Campus Meridian — Stationery Set</title>
<link rel="stylesheet" href="https://fonts.googleapis.com/css2?family=PT+Sans:wght@400;700&display=swap">
<style>
:root{
  --tiffany:#5ff5d0;
  --ink:#111111;
  --paper:#ffffff;
  --paper-shade:#e4e4e4;
  --rule:#222222;
  --stage:#ecebe8;
  --text:#1c1c1c;
}
*{box-sizing:border-box;margin:0;padding:0}
html,body{width:1200px;height:540px;overflow:hidden;background:var(--stage)}
body{font-family:"PT Sans",Arial,sans-serif;color:var(--text);position:relative}
.sheet{position:absolute;background:var(--paper);box-shadow:0 1px 3px rgba(0,0,0,.18)}
.letterhead{left:24px;top:42px;width:334px;height:432px}
.fax-sheet{left:378px;top:42px;width:334px;height:432px}

.brand{position:absolute;display:flex;align-items:center;gap:4px;font-weight:700;color:var(--ink);line-height:1;text-transform:uppercase;letter-spacing:.02em}
.brand-mark{display:block;background:var(--tiffany)}
.sheet .brand{left:14px;top:18px;font-size:13px}
.sheet .brand-mark{width:11px;height:11px}

.contact{position:absolute;left:248px;top:14px;border-left:1px solid var(--ink);padding-left:5px;font-size:5.4px;line-height:8px;color:var(--text)}
.contact li{list-style:none;display:flex;align-items:center;gap:3px}
.contact svg{width:5px;height:5px;flex:none}

.sheet-footer{position:absolute;left:0;right:0;bottom:0;height:26px}
.footer-mark{position:absolute;left:10px;top:0;width:12px;height:12px;background:var(--tiffany)}
.tagline{position:absolute;left:37px;top:5px;font-size:5.6px}
.address{position:absolute;right:12px;top:5px;font-size:6px;letter-spacing:.04em}
.footer-rule{position:absolute;left:0;right:0;top:14px;height:2px;background:var(--rule)}
.footer-band{position:absolute;left:0;right:0;bottom:0;height:6px;background:var(--tiffany)}

.fax-title{position:absolute;left:16px;top:98px;font-size:20px;font-weight:400;letter-spacing:.02em}
.fax-fields{position:absolute;left:16px;top:132px;width:302px}
.fax-row{display:flex;gap:18px;height:18px;align-items:flex-end}
.fax-field{border-bottom:1px solid var(--ink);font-size:5.4px;padding-bottom:2px}
.fax-field.left{width:160px}
.fax-field.right{width:124px;margin-left:auto}
.fax-options{position:absolute;left:16px;top:218px;width:302px;display:flex;justify-content:space-between;font-size:5.4px}
.fax-options span{display:flex;align-items:center;gap:4px}
.fax-options i{display:block;width:7px;height:7px;border:1px solid var(--ink)}

.envelope-back{position:absolute;left:793px;top:46px;width:375px;height:168px;background:var(--paper);box-shadow:0 1px 3px rgba(0,0,0,.18)}
.envelope-flap{position:absolute;left:0;top:0;width:375px;height:72px}
.envelope-inner{position:absolute;left:782px;top:120px;width:374px;height:70px}
.envelope-front{position:absolute;left:756px;top:204px;width:374px;height:166px;background:linear-gradient(100deg,var(--paper) 0%,#f1f1f1 55%,var(--paper-shade) 100%);box-shadow:0 1px 4px rgba(0,0,0,.2)}
.envelope-front .brand{left:14px;top:16px;font-size:13px}
.envelope-front .brand-mark{width:11px;height:11px}
.envelope-address{position:absolute;left:10px;top:52px;font-size:6px}
.envelope-footer{position:absolute;left:0;right:0;bottom:0;height:30px}
.envelope-footer .footer-mark{left:10px;top:0;width:14px;height:14px}
.envelope-url{position:absolute;left:40px;top:8px;font-size:6px}
.envelope-footer .footer-rule{top:18px;height:2px;left:32px}
.envelope-footer .footer-band{height:8px}

.card{position:absolute;width:138px;height:80px;box-shadow:0 1px 3px rgba(0,0,0,.2)}
.card-front{left:726px;top:398px;background:linear-gradient(100deg,#fff 0%,#efefef 100%)}
.card-front .brand{left:6px;top:8px;font-size:8px;gap:3px}
.card-front .brand-mark{width:7px;height:7px}
.card-tagline{position:absolute;left:4px;top:30px;font-size:3.4px}
.card-name{position:absolute;left:78px;top:30px;font-size:5.4px;font-weight:700}
.card-title{position:absolute;left:78px;top:37px;font-size:3.6px}
.card-contact{position:absolute;left:78px;top:48px;font-size:3.4px;line-height:5px;list-style:none}
.card-front .corner-mark{position:absolute;left:5px;bottom:5px;width:7px;height:7px;background:var(--tiffany)}
.card-front .card-rule{position:absolute;left:16px;right:0;bottom:6px;height:1px;background:var(--rule)}
.card-front .card-band{position:absolute;left:0;right:0;bottom:0;height:3px;background:var(--tiffany)}
.card-back{top:400px;display:flex;flex-direction:column;align-items:center;justify-content:center;gap:6px;color:#fff}
.card-back.dark{left:875px;background:var(--ink)}
.card-back.bright{left:1023px;width:137px;background:var(--tiffany)}
.card-back .brand{position:static;color:#fff;font-size:10px;gap:3px}
.card-back .brand-mark{width:8px;height:8px;background:#fff}
.card-back.dark .brand-mark{background:var(--tiffany)}
.card-url{font-size:5px}
</style>
</head>
<body>

<svg width="0" height="0" style="position:absolute" aria-hidden="true">
  <symbol id="icon-phone" viewBox="0 0 10 10"><circle cx="5" cy="5" r="4.5" fill="none" stroke="#111" stroke-width="1"/><path d="M3.3 2.6c.4 2 1.8 3.7 3.6 4.6l.6-1-1-.7-.5.5C5 5.5 4.6 5 4.3 4.2l.5-.4-.5-1.2z" fill="#111"/></symbol>
  <symbol id="icon-mail" viewBox="0 0 10 10"><rect x="0.5" y="2" width="9" height="6" fill="#111"/></symbol>
  <symbol id="icon-web" viewBox="0 0 10 10"><circle cx="5" cy="5" r="4.5" fill="#111"/><path d="M.5 5h9M5 .5v9" stroke="#fff" stroke-width=".7"/></symbol>
</svg>

<section class="sheet letterhead" aria-label="Letterhead">
  <div class="brand"><span class="brand-mark"></span>Campus Meridian</div>
  <ul class="contact">
    <li><svg><use href="#icon-phone"/></svg>+91 20 4417 0921</li>
    <li><svg><use href="#icon-phone"/></svg>+91 20 4417 0935</li>
    <li><svg><use href="#icon-mail"/></svg>hello@campusmeridian.com</li>
    <li><svg><use href="#icon-web"/></svg>www.campusmeridian.com</li>
  </ul>
  <footer class="sheet-footer">
    <span class="footer-mark"></span>
    <span class="tagline">Experience • Education • Excellence</span>
    <span class="address">Street Name, City Name State Zipcode</span>
    <span class="footer-rule"></span>
    <span class="footer-band"></span>
  </footer>
</section>

<section class="sheet fax-sheet" aria-label="Fax cover sheet">
  <div class="brand"><span class="brand-mark"></span>Campus Meridian</div>
  <ul class="contact">
    <li><svg><use href="#icon-phone"/></svg>+91 20 4417 0921</li>
    <li><svg><use href="#icon-phone"/></svg>+91 20 4417 0935</li>
    <li><svg><use href="#icon-mail"/></svg>hello@campusmeridian.com</li>
    <li><svg><use href="#icon-web"/></svg>www.campusmeridian.com</li>
  </ul>
  <h1 class="fax-title">FAX</h1>
  <div class="fax-fields">
    <div class="fax-row"><span class="fax-field left">To :</span><span class="fax-field right">From :</span></div>
    <div class="fax-row"><span class="fax-field left">Fax :</span><span class="fax-field right">Pages :</span></div>
    <div class="fax-row"><span class="fax-field left">Phone :</span><span class="fax-field right">Date :</span></div>
    <div class="fax-row"><span class="fax-field left">Re :</span><span class="fax-field right">CC :</span></div>
  </div>
  <div class="fax-options">
    <span><i></i>Urgent</span>
    <span><i></i>For Review</span>
    <span><i></i>Please Comment</span>
    <span><i></i>Please Reply</span>
    <span><i></i>Please Recycle</span>
  </div>
  <footer class="sheet-footer">
    <span class="footer-mark"></span>
    <span class="tagline">Experience • Education • Excellence</span>
    <span class="address">Street Name, City Name State Zipcode</span>
    <span class="footer-rule"></span>
    <span class="footer-band"></span>
  </footer>
</section>

<div class="envelope-back" aria-label="Envelope back">
  <svg class="envelope-flap" viewBox="0 0 375 72" preserveAspectRatio="none">
    <path d="M0 0H375V10C340 40 280 62 230 66H145C95 62 35 40 0 10Z" fill="#111"/>
  </svg>
</div>
<svg class="envelope-inner" viewBox="0 0 374 70" preserveAspectRatio="none" aria-hidden="true">
  <rect width="374" height="70" fill="#f2f2f2"/>
  <path d="M0 0H374V8C345 40 290 62 240 66H134C84 62 29 40 0 8Z" fill="#5ff5d0"/>
</svg>

<section class="envelope-front" aria-label="Envelope front">
  <div class="brand"><span class="brand-mark"></span>Campus Meridian</div>
  <p class="envelope-address">Street Name, City Name, State Zipcode</p>
  <footer class="envelope-footer">
    <span class="footer-mark"></span>
    <span class="envelope-url">www.campusmeridian.com</span>
    <span class="footer-rule"></span>
    <span class="footer-band"></span>
  </footer>
</section>

<section class="card card-front" aria-label="Business card front">
  <div class="brand"><span class="brand-mark"></span>Campus Meridian</div>
  <p class="card-tagline">Experience • Education • Excellence</p>
  <p class="card-name">Your Name</p>
  <p class="card-title">Title</p>
  <ul class="card-contact">
    <li>+91 20 4417 0921</li>
    <li>+91 20 4417 0935</li>
    <li>hello@campusmeridian.com</li>
    <li>www.campusmeridian.com</li>
  </ul>
  <span class="corner-mark"></span>
  <span class="card-rule"></span>
  <span class="card-band"></span>
</section>

<section class="card card-back dark" aria-label="Business card back, black">
  <div class="brand"><span class="brand-mark"></span>Campus Meridian</div>
  <p class="card-url">www.campusmeridian.com</p>
</section>

<section class="card card-back bright" aria-label="Business card back, tiffany">
  <div class="brand"><span class="brand-mark"></span>Campus Meridian</div>
  <p class="card-url">www.campusmeridian.com</p>
</section>

</body>
</html>
```